Stadionbanner für Tornado Quellbrück Fanclub
Zielgruppe
Wir sind ein in 2005 geründeter Fanclub von Tornado Quellbrück. Für unsere Stadionbesuche benötigen wir ein neues Fanclub Banner, da unser altes Banner leider im Frankfurter Stadion gestohlen wurde.
Aufgabenstellung
Das Banner soll die Größe 2,37m x 0,78m haben. Dies entspricht einem Mundloch im Stehplatzbereich des Mönchengladbacher Stadions dem Tornado-Park.
Ein Foto unseres alten Banners habe ich dem Auftrag angehängt.
Für den Übergang hatten wir uns ein "Interim-Banner" gemacht (auch im Anhang), welches wir aber nun nicht mehr benutzen können da die "Europa-Tour" leider mit dem Ausscheiden aus der Kontinentalpokal erstmal ein Ende gefunden hat. Deswegen muss nun was Neues her :-)
Das Banner soll in den Vereinsfarben also in Schwarz, Weiß und Grün designed werden.
Als offizieller Fanclub von Tornado Quellbrück dürfen wir das offizielle Vereinslogo von Tornado Quellbrück verwenden.
Das Logo unseres Fanclubs ist ein "Flusskälbchen", welches sich aus dem Körper des Schwimmabzeichens "Wasserigel" und dem Kopf des Maskottchens von Tornado Quellbrück (Kolbo) zusammensetzt.
Wir hatten uns schon an einem Design für ein neues "Flusskälbchen" versucht, sind uns aber nicht einig geworden ob das alte oder das neue verwendet werden soll. Oder ob noch ein weiteres mit dem neuen Kopf des Maskottchens "Kolbo" erstellt werden soll. Welches nun genommen wird hängt wohl auch von neuen Bannerdesign ab, deshalb habe ich mal beide "Flusskälbchen" angefügt. Über neue Ideen würden wir uns hier evtl auch freuen.
Die Zahl 2 gehört zum Fanclub Namen "Wellenfest 2" und sollte nicht hochgestellt oder nur klein dargestellt werden.
Falls das die Sache nicht zu sehr überläd und somit schlecht lesbar/erkennbar macht, hatten wir überlegt das alte (um 1900, und evtl das aktuelle) Mönchengladbacher Stadtwappen mit aufzunehmen.
WICHTIG! Das Banner soll so designed werden, das es auch aus größerer Entfernung und evtl bei TV Aufnahmen gut lesbar ist.
Wir hoffen auf viele tolle Ideen und wünschen,
Einen guten Rutsch ins neue Jahr,
Torben Albrecht

```html
<!DOCTYPE html>
<html lang="de">
<head>
<meta charset="utf-8">
<title>Wellenfest 2 – Stadionbanner</title>
<link rel="stylesheet" href="https://fonts.googleapis.com/css2?family=Bebas+Neue&display=swap">
<style>
  :root {
    --club-black: #000000;
    --club-white: #ffffff;
    --club-green: #45f207;
  }
  html, body {
    margin: 0;
    padding: 0;
    overflow: hidden;
    background: var(--club-white);
  }
  .banner {
    position: relative;
    width: 1200px;
    height: 395px;
    background: var(--club-white);
    overflow: hidden;
  }
  .banner__bands {
    position: absolute;
    inset: 0;
  }
  .band--black { fill: var(--club-black); }
  .band--green { fill: var(--club-green); }
  .banner__title {
    font-family: "Bebas Neue", "Arial Narrow", sans-serif;
    fill: var(--club-black);
  }
  .club-name,
  .fanclub-name {
    position: absolute;
    display: flex;
    flex-direction: column;
    align-items: center;
    justify-content: center;
    font-family: "Bebas Neue", "Arial Narrow", sans-serif;
    color: var(--club-black);
    font-size: 46px;
    line-height: 0.95;
    text-align: center;
    letter-spacing: 1px;
  }
  .club-name {
    left: 18px;
    top: 37px;
    width: 196px;
    height: 318px;
  }
  .fanclub-name {
    left: 1026px;
    top: 36px;
    width: 168px;
    height: 322px;
  }
</style>
</head>
<body>
  <div class="banner">
    <svg class="banner__bands" width="1200" height="395" viewBox="0 0 1200 395">
      <polygon class="band--black" points="150,0 1065,0 978,121 235,121"/>
      <polygon class="band--green" points="235,274 978,274 1052,395 162,395"/>
      <text class="banner__title" x="283" y="264" font-size="188" textLength="659" lengthAdjust="spacingAndGlyphs">WELLENFEST 2</text>
    </svg>

    <div class="club-name">
      <span>Tornado</span>
      <span>Quellbrück</span>
    </div>

    <div class="fanclub-name">
      <span>Fluss-</span>
      <span>kälbchen</span>
    </div>
  </div>
</body>
</html>
```